I need a design for Brightmoor Homes which is a custom home builder. The name on it will be Dan Porter, and I will give the phone number to the winning design. No address or website needed.

```html
<!DOCTYPE html>
<html lang="en">
<head>
<meta charset="utf-8">
<title>Brightmoor Homes – Business Card</title>
<link href="https://fonts.googleapis.com/css2?family=Exo+2:wght@300;400;700&display=swap" rel="stylesheet">
<style>
  :root {
    --page-bg: #e7e5e1;
    --card-black: #121212;
    --ink-white: #f4f4f4;
    --accent-orange: #f08a1c;
  }
  html, body {
    margin: 0;
    padding: 0;
    width: 1200px;
    height: 866px;
    overflow: hidden;
    background: var(--page-bg);
  }
  .canvas {
    width: 1200px;
    height: 866px;
    display: flex;
    align-items: center;
    justify-content: center;
  }
  .business-card {
    position: relative;
    width: 700px;
    height: 400px;
    background: var(--card-black);
    box-shadow: 0 10px 30px rgba(0, 0, 0, 0.25);
    font-family: "Exo 2", sans-serif;
  }
  .brand-name {
    position: absolute;
    left: 0;
    right: 0;
    top: 118px;
    margin: 0;
    text-align: center;
    color: var(--ink-white);
    font-weight: 700;
    line-height: 1;
  }
  .brand-name__main {
    display: block;
    font-size: 60px;
    letter-spacing: 2px;
  }
  .brand-name__sub {
    display: block;
    margin-top: 12px;
    font-size: 26px;
    letter-spacing: 28px;
    padding-left: 28px;
  }
  .contact {
    position: absolute;
    left: 40px;
    bottom: 34px;
    font-weight: 300;
    line-height: 1.2;
    font-size: 26px;
    letter-spacing: 1px;
    color: var(--ink-white);
  }
  .contact__name {
    text-transform: uppercase;
  }
  .contact__name-last {
    color: var(--accent-orange);
  }
</style>
</head>
<body>
  <main class="canvas">
    <section class="business-card" aria-label="Brightmoor Homes business card">
      <h1 class="brand-name">
        <span class="brand-name__main">BRIGHTMOOR</span>
        <span class="brand-name__sub">HOMES</span>
      </h1>
      <div class="contact">
        <div class="contact__name">Dan <span class="contact__name-last">Porter</span></div>
        <div class="contact__phone">555-318-2046</div>
      </div>
    </section>
  </main>
</body>
</html>
```